UHT milk packaging Design, (Package Design and Outer Carton Design)

Create a Packaging Design
We would like to you to design a UHT milk packaging. We would need our brand logo on the box (Solvine or Brackwell). At present, we do not have a logo design, only the brand name. The Name of the product will be "Full Cream Milk", "Skim Milk", "Lite Milk"

We use Quadra Pak packaging,
Dimensions of 1L product: 90mm*58mm*195mm
Dimensions of 250ml product: 63mm*40mm*106mm

It should also include:
Barcode placeholder
Area for ingredients
1L and 250ml

Upload files are photoes of other Quadra Pak packaging

The final design should communicate:
Freshness
Healthy
Modern
Striking

Subsequently, we also have other products packaging that need to be designed, such as muesli, meat, etc

Target Market(s)

family consumption

Font styles to use
Decorative

Requirements
Must have
• Our brand logo (BRACKWELL);
• Make people feel fresh and healthy
Nice to have
• Bright colors;
• Attractive picture

```html
<!DOCTYPE html>
<html lang="en">
<head>
<meta charset="utf-8">
<title>Brackwell UHT Milk – Carton Range</title>
<link href="https://fonts.googleapis.com/css2?family=Montserrat:wght@400;500&family=Playfair+Display:ital,wght@1,400&display=swap" rel="stylesheet">
<style>
  :root {
    --page-bg: #eceeef;
    --white: #ffffff;
    --brand-gold: #9c8545;

    --skim-panel: #7ef0e2;
    --skim-side: #8fe6dc;
    --skim-check-a: #c9f1ec;
    --skim-check-b: #9fe3da;
    --skim-edge: #b9d4d6;

    --lite-panel: #6cf26a;
    --lite-side: #7fe27d;
    --lite-check-a: #e6f7b8;
    --lite-check-b: #86ec84;
    --lite-edge: #e5ef5c;

    --cream-panel: #fdc17f;
    --cream-side: #d8b66b;
    --cream-check-a: #f3c99c;
    --cream-check-b: #8fe39a;
    --cream-edge: #cf9a58;
  }

  * { box-sizing: border-box; margin: 0; padding: 0; }

  html, body {
    width: 1200px;
    height: 800px;
    overflow: hidden;
    background: var(--page-bg);
  }

  .range {
    width: 1200px;
    height: 800px;
    display: flex;
    justify-content: center;
    align-items: center;
    gap: 60px;
  }

  .carton {
    display: flex;
    height: 620px;
    box-shadow: 0 14px 30px rgba(0, 0, 0, 0.08);
  }

  /* Side panel */
  .carton__side {
    position: relative;
    width: 50px;
    height: 100%;
    overflow: hidden;
  }
  .carton__side-check {
    position: absolute;
    inset: 0;
    background: linear-gradient(180deg, var(--check-a), var(--check-b));
  }
  .carton__side-panel {
    position: absolute;
    left: 0; right: 0; bottom: 0;
    top: 205px;
    background: var(--side);
    border-radius: 25px 25px 0 0;
  }
  .ingredients-area {
    position: absolute;
    left: 6px; right: 6px;
    top: 80px;
    height: 265px;
    background: var(--white);
  }

  /* Front panel */
  .carton__front {
    position: relative;
    width: 260px;
    height: 100%;
    overflow: hidden;
    box-shadow: inset 0 0 0 5px rgba(255, 255, 255, 0.55);
  }
  .carton__check {
    position: absolute;
    inset: 0;
    background: linear-gradient(160deg, var(--check-a), var(--check-b));
  }
  .carton__arch {
    position: absolute;
    left: 0; top: 0;
    width: 260px;
    height: 620px;
  }
  .carton__arch path {
    fill: var(--panel);
    stroke: var(--edge);
    stroke-width: 2;
  }

  .brand {
    position: absolute;
    top: 48px;
    left: 30px;
    display: flex;
    align-items: center;
    gap: 6px;
    font-family: "Montserrat", sans-serif;
    font-weight: 500;
    font-size: 14px;
    letter-spacing: 0.5px;
    color: var(--brand-gold);
  }
  .brand__mark {
    width: 10px;
    height: 10px;
    background: var(--brand-gold);
  }

  .variant {
    position: absolute;
    left: 36px;
    bottom: 250px;
    font-family: "Montserrat", sans-serif;
    font-weight: 400;
    font-size: 22px;
    line-height: 0.9;
    color: var(--white);
  }
  .product-name {
    position: absolute;
    left: 30px;
    top: 350px;
    font-family: "Playfair Display", serif;
    font-style: italic;
    font-weight: 400;
    font-size: 92px;
    line-height: 1;
    color: var(--white);
  }

  .milk-splash {
    position: absolute;
    left: 0;
    right: 0;
    bottom: 0;
    height: 160px;
    background:
      radial-gradient(ellipse 60% 55% at 50% 80%, rgba(255,255,255,0.98), rgba(255,255,255,0.75) 55%, rgba(255,255,255,0) 100%);
  }

  .volume {
    position: absolute;
    left: 0; right: 0;
    bottom: 14px;
    text-align: center;
    font-family: "Montserrat", sans-serif;
    font-weight: 500;
    font-size: 16px;
    color: var(--edge);
  }

  .carton--skim {
    --panel: var(--skim-panel);
    --side: var(--skim-side);
    --check-a: var(--skim-check-a);
    --check-b: var(--skim-check-b);
    --edge: var(--skim-edge);
  }
  .carton--lite {
    --panel: var(--lite-panel);
    --side: var(--lite-side);
    --check-a: var(--lite-check-a);
    --check-b: var(--lite-check-b);
    --edge: var(--lite-edge);
  }
  .carton--lite .volume { color: #4aa84a; }
  .carton--cream {
    --panel: var(--cream-panel);
    --side: var(--cream-side);
    --check-a: var(--cream-check-a);
    --check-b: var(--cream-check-b);
    --edge: var(--cream-edge);
  }
</style>
</head>
<body>
<main class="range">

  <article class="carton carton--skim">
    <div class="carton__side">
      <div class="carton__side-check" role="img" aria-label="Blue gingham check pattern"></div>
      <div class="carton__side-panel">
        <div class="ingredients-area" role="img" aria-label="Space for ingredients"></div>
      </div>
    </div>
    <div class="carton__front">
      <div class="carton__check" role="img" aria-label="Blue gingham check pattern"></div>
      <svg class="carton__arch" viewBox="0 0 260 620" aria-hidden="true">
        <path d="M0 620 V262 C10 215 60 192 130 192 C200 192 250 215 260 262 V620 Z"/>
      </svg>
      <div class="brand"><span class="brand__mark"></span>BRACKWELL</div>
      <p class="variant">skim</p>
      <p class="product-name">milk</p>
      <div class="milk-splash" role="img" aria-label="Milk splash illustration"></div>
      <p class="volume">1l</p>
    </div>
  </article>

  <article class="carton carton--lite">
    <div class="carton__side">
      <div class="carton__side-check" role="img" aria-label="Green and yellow gingham check pattern"></div>
      <div class="carton__side-panel">
        <div class="ingredients-area" role="img" aria-label="Space for ingredients"></div>
      </div>
    </div>
    <div class="carton__front">
      <div class="carton__check" role="img" aria-label="Green and yellow gingham check pattern"></div>
      <svg class="carton__arch" viewBox="0 0 260 620" aria-hidden="true">
        <path d="M0 620 V262 C10 215 60 192 130 192 C200 192 250 215 260 262 V620 Z"/>
      </svg>
      <div class="brand"><span class="brand__mark"></span>BRACKWELL</div>
      <p class="variant">lite</p>
      <p class="product-name">milk</p>
      <div class="milk-splash" role="img" aria-label="Milk splash illustration"></div>
      <p class="volume">1l</p>
    </div>
  </article>

  <article class="carton carton--cream">
    <div class="carton__side">
      <div class="carton__side-check" role="img" aria-label="Orange and green gingham check pattern"></div>
      <div class="carton__side-panel">
        <div class="ingredients-area" role="img" aria-label="Space for ingredients"></div>
      </div>
    </div>
    <div class="carton__front">
      <div class="carton__check" role="img" aria-label="Orange and green gingham check pattern"></div>
      <svg class="carton__arch" viewBox="0 0 260 620" aria-hidden="true">
        <path d="M0 620 V262 C10 215 60 192 130 192 C200 192 250 215 260 262 V620 Z"/>
      </svg>
      <div class="brand"><span class="brand__mark"></span>BRACKWELL</div>
      <p class="variant">full<br>cream</p>
      <p class="product-name">milk</p>
      <div class="milk-splash" role="img" aria-label="Milk splash illustration"></div>
      <p class="volume">1l</p>
    </div>
  </article>

</main>
</body>
</html>
```